Stylish Business Card for Modern hair salon

I need a simple business card design using our salon logo and colours that are in the logo. We service clients of all ages but predominantly those in the 18 to 55 age range. We have a young staff and are looking to have a card that will present a modern and clean image that represents who we are. The card should be in black and white same as our logo. Minimal use of other colours is allowed.

Industry/Entity Type

Hair And Beauty

Contact Information for Business Card

The design should have the following information
salon name - TR Hair Studio
address - 2751 Birchfield Rd.E. Mississauga, ON L7P3K2
phone - 905 614-2870
website - trhairexample.ca
instagram - tr.hairstudio
twitter - @TR_HairStudio

Colors
000000
ffffff
474747

Requirements
Must have
• simple design, salon name, address, phone, website, instagram, twitter info
• Back of card should have the following:
• YOUR NEXT APPOINTMENT
• DATE
• TIME
Nice to have
• simple design, clear to see and read,
• predominantly black and white colour, minimal use of other colours is ok
Should not have
• many colours, various fonts

```html
<!DOCTYPE html>
<html lang="en">
<head>
<meta charset="utf-8">
<title>TR Hair Studio – Business Card</title>
<link rel="stylesheet" href="https://fonts.googleapis.com/css2?family=Questrial&display=swap">
<style>
  :root {
    --ink: #000000;
    --paper: #ffffff;
    --grey: #474747;
    --faint: #efefef;
    --stage: #e4e4e4;
  }
  * { margin: 0; padding: 0; box-sizing: border-box; }
  html, body {
    width: 1200px; height: 880px; overflow: hidden;
    background: var(--stage);
    font-family: "Questrial", "Century Gothic", sans-serif;
    color: var(--ink);
  }
  .canvas {
    width: 1200px; height: 880px;
    display: flex; flex-direction: column; align-items: center; justify-content: center;
    gap: 30px;
  }
  .card {
    position: relative;
    width: 700px; height: 400px;
    background: var(--paper);
    box-shadow: 0 6px 18px rgba(0,0,0,0.18);
    overflow: hidden;
  }

  /* Back: appointment card */
  .back__mark {
    position: absolute; left: 0; right: 0; top: 95px;
    text-align: center;
    font-size: 170px; line-height: 1;
    color: var(--faint);
    letter-spacing: 4px;
    white-space: nowrap;
  }
  .back__heading {
    position: absolute; left: 190px; top: 140px;
    font-size: 15px; letter-spacing: 1.2px;
  }
  .field {
    position: absolute;
    display: flex; align-items: flex-end; gap: 12px;
    font-size: 15px; letter-spacing: 1px;
  }
  .field__line {
    display: block; height: 0;
    border-bottom: 1.5px solid var(--ink);
    margin-bottom: 3px;
  }
  .field--time { left: 430px; top: 132px; }
  .field--time .field__line { width: 210px; }
  .field--date { left: 120px; top: 250px; }
  .field--date .field__line { width: 250px; }

  /* Front: contact card */
  .front__name-mark {
    position: absolute; left: 40px; width: 300px; top: 160px;
    text-align: center;
    font-size: 72px; line-height: 1;
    color: var(--ink);
    white-space: nowrap;
  }
  .front__divider {
    position: absolute; left: 365px; top: 80px;
    width: 0; height: 240px;
    border-left: 1.5px solid var(--grey);
  }
  .contact {
    position: absolute; left: 400px; top: 92px;
    font-size: 15px; line-height: 1.35;
  }
  .contact__studio { font-size: 22px; margin-bottom: 20px; }
  .contact__address { margin-bottom: 10px; }
  .contact__list { list-style: none; }
  .contact__item { display: flex; align-items: center; gap: 8px; height: 24px; }
  .contact__icon { width: 16px; height: 16px; flex: none; }
</style>
</head>
<body>
<main class="canvas">

  <section class="card card--back" aria-label="Appointment card">
    <div class="back__mark" aria-hidden="true">TR Hair</div>
    <p class="back__heading">YOUR NEXT APPOINTMENT</p>
    <div class="field field--time"><span>TIME</span><span class="field__line"></span></div>
    <div class="field field--date"><span>DATE</span><span class="field__line"></span></div>
  </section>

  <section class="card card--front" aria-label="Contact card">
    <div class="front__name-mark">TR Hair</div>
    <div class="front__divider"></div>
    <div class="contact">
      <p class="contact__studio">TR Hair Studio</p>
      <p class="contact__address">2751 Birchfield Rd.E.<br>Mississauga, ON L7P3K2</p>
      <ul class="contact__list">
        <li class="contact__item">
          <svg class="contact__icon" viewBox="0 0 16 16" aria-hidden="true">
            <circle cx="8" cy="8" r="8" fill="var(--ink)"/>
            <path d="M5.2 4.2c.4-.3.9-.2 1.1.2l.7 1.3c.2.4.1.8-.2 1l-.5.4c.4.9 1.1 1.6 2 2l.4-.5c.3-.3.7-.4 1-.2l1.3.7c.4.2.5.7.2 1.1l-.5.7c-.4.5-1.1.6-1.7.3-2-1-3.6-2.6-4.6-4.6-.3-.6-.2-1.3.3-1.7z" fill="var(--paper)"/>
          </svg>
          <span>905 614-2870</span>
        </li>
        <li class="contact__item">
          <svg class="contact__icon" viewBox="0 0 16 16" aria-hidden="true">
            <circle cx="8" cy="8" r="8" fill="var(--ink)"/>
            <circle cx="8" cy="8" r="4.5" fill="none" stroke="var(--paper)" stroke-width="1"/>
            <path d="M3.5 8h9M8 3.5c-2 2.5-2 6.5 0 9M8 3.5c2 2.5 2 6.5 0 9" fill="none" stroke="var(--paper)" stroke-width="0.9"/>
          </svg>
          <span>trhairexample.ca</span>
        </li>
        <li class="contact__item">
          <svg class="contact__icon" viewBox="0 0 16 16" aria-hidden="true"><circle cx="8" cy="8" r="8" fill="var(--ink)"/></svg>
          <span>tr.hairstudio</span>
        </li>
        <li class="contact__item">
          <svg class="contact__icon" viewBox="0 0 16 16" aria-hidden="true"><circle cx="8" cy="8" r="8" fill="var(--ink)"/></svg>
          <span>@TR_HairStudio</span>
        </li>
      </ul>
    </div>
  </section>

</main>
</body>
</html>
```